Veltharion Email Direct Marketing Campaign

This is an email campaign. The copy is attached. Also attached is our logo and business card. You can get some design ideas from those and our website (www.veltharion-example.com). But don't let those limit your ideas. We are open to suggestions. We want a great looking campaign that is in line with current clean design trends (including flat design) and marketing messaging.
Updates

Hi Designers. This is not a home page design or a logo redesign. This is the design of an email campaign which will arrive in people's inboxes as a promotion. Do not take wording from the website. All wording is in the text PDF attached. No coding is required. Thanks

Industry/Entity Type

Marketing

```html
<!DOCTYPE html>
<html lang="en">
<head>
<meta charset="utf-8">
<title>Veltharion Email Campaign</title>
<link rel="stylesheet" href="https://fonts.googleapis.com/css2?family=Open+Sans:ital,wght@0,400;0,600;0,700;1,400&display=swap">
<style>
  :root {
    --page-bg: #ededed;
    --brand-blue: #0459aa;
    --blue-facet: #4177ba;
    --brand-red: #ee1d25;
    --ink: #2b3550;
    --body-ink: #3a3f4c;
    --panel-grey: #f7f7f7;
    --rule: #e2e2e2;
    --unsub-bg: #dedede;
    --white: #ffffff;
  }
  * { margin: 0; padding: 0; box-sizing: border-box; }
  html, body {
    width: 865px; height: 1200px; overflow: hidden;
    background: var(--page-bg);
    font-family: "Open Sans", Arial, sans-serif;
    color: var(--ink);
  }
  .stage {
    position: relative; width: 800px; height: 1110px;
    transform: scale(1.08125); transform-origin: top left;
  }
  .preheader {
    position: absolute; top: 47px; left: 0; width: 800px;
    text-align: center; font-size: 11.5px; letter-spacing: 1.6px;
    text-transform: uppercase; color: var(--ink);
  }
  .preheader strong { font-weight: 700; }
  .email { position: absolute; left: 100px; top: 82px; width: 600px; }

  .masthead {
    position: relative; height: 184px; background: var(--brand-blue); overflow: hidden;
  }
  .masthead svg.facets { position: absolute; inset: 0; }
  .wordmark {
    position: absolute; top: 76px; left: 0; width: 100%;
    text-align: center; color: var(--white);
    font-size: 40px; font-weight: 600; line-height: 52px; letter-spacing: 0.3px;
  }
  .site-link {
    position: absolute; bottom: 0; left: 220px; width: 160px;
    text-align: center; color: var(--white); font-size: 13px; letter-spacing: 0.5px;
    padding-bottom: 6px; border-bottom: 4px solid var(--brand-red);
  }

  .services { height: 319px; background: var(--white); text-align: center; padding-top: 64px; }
  .services h1 { font-size: 17px; font-weight: 700; letter-spacing: 2.2px; }
  .service-list { display: flex; justify-content: center; gap: 54px; margin-top: 32px; list-style: none; }
  .service { width: 100px; font-size: 11.5px; letter-spacing: 1px; }
  .service .badge { width: 100px; height: 100px; border-radius: 50%; background: var(--brand-blue); display: block; }
  .service-title { display: block; margin-top: 16px; font-weight: 700; white-space: nowrap; margin-left: -30px; margin-right: -30px; }
  .service-sub { display: block; margin-top: 4px; white-space: nowrap; margin-left: -30px; margin-right: -30px; }

  .about { position: relative; height: 255px; background: var(--panel-grey); padding: 35px 0 0 68px; }
  .about h2 { font-size: 12.5px; font-weight: 700; letter-spacing: 0.8px; line-height: 18px; width: 470px; }
  .about h3 { margin-top: 18px; font-size: 14px; font-weight: 700; letter-spacing: 0.8px; }
  .benefits { list-style: none; margin-top: 16px; }
  .benefits li { font-size: 12px; letter-spacing: 0.7px; color: var(--body-ink); line-height: 16px; margin-bottom: 20px; }
  .about .pin { position: absolute; left: 427px; top: 66px; }

  .contact { position: relative; height: 113px; background: var(--white); padding: 17px 30px 0; }
  .contact .rule { border-top: 2px solid var(--rule); }
  .contact-details { margin-top: 16px; font-size: 11px; line-height: 18px; color: var(--body-ink); }
  .contact-details strong { color: var(--ink); }
  .contact-details em { font-style: italic; }
  .contact-domain { position: absolute; right: 30px; top: 31px; font-size: 14px; font-weight: 700; color: var(--ink); }

  .unsubscribe { height: 40px; background: var(--unsub-bg); text-align: center; font-size: 11px; line-height: 40px; color: var(--body-ink); }
  .unsubscribe a { color: var(--ink); font-weight: 700; }
</style>
</head>
<body>
<div class="stage">
  <p class="preheader"><strong>Veltharion</strong> your trusted partner now and in the future.</p>

  <main class="email">
    <header class="masthead">
      <svg class="facets" width="600" height="184" viewBox="0 0 600 184" aria-hidden="true">
        <polygon points="0,33 70,102 0,170" fill="var(--blue-facet)"/>
        <polygon points="600,33 530,102 600,170" fill="var(--blue-facet)"/>
      </svg>
      <div class="wordmark">Veltharion</div>
      <div class="site-link">www.veltharion-example.com</div>
    </header>

    <section class="services">
      <h1>LET US HELP YOUR BUSINESS</h1>
      <ul class="service-list">
        <li class="service">
          <svg class="badge" viewBox="0 0 100 100" aria-hidden="true">
            <circle cx="50" cy="50" r="50" fill="var(--brand-blue)"/>
            <rect x="22" y="22" width="56" height="55" fill="#fff"/>
            <rect x="29" y="28" width="26" height="6" fill="#d3d8e2"/>
            <rect x="59" y="28" width="12" height="6" fill="#d3d8e2"/>
            <circle cx="32" cy="41" r="3" fill="#d3d8e2"/><circle cx="43" cy="41" r="3" fill="#d3d8e2"/>
            <circle cx="55" cy="41" r="3" fill="#d3d8e2"/><circle cx="67" cy="41" r="3" fill="#d3d8e2"/>
            <rect x="29" y="48" width="42" height="6" fill="#d3d8e2"/>
          </svg>
          <span class="service-title">BUILD A</span>
          <span class="service-sub">GREAT WEBSITE</span>
        </li>
        <li class="service">
          <svg class="badge" viewBox="0 0 100 100" role="img" aria-label="Handshake illustration">
            <circle cx="50" cy="50" r="50" fill="var(--brand-blue)"/>
            <ellipse cx="50" cy="52" rx="26" ry="18" fill="#eee3b0"/>
          </svg>
          <span class="service-title">ENGAGE WITH</span>
          <span class="service-sub">YOUR CUSTOMERS</span>
        </li>
        <li class="service">
          <svg class="badge" viewBox="0 0 100 100" aria-hidden="true">
            <circle cx="50" cy="50" r="50" fill="var(--brand-blue)"/>
            <line x1="58" y1="58" x2="76" y2="76" stroke="#5a5d66" stroke-width="6" stroke-linecap="round"/>
            <circle cx="47" cy="45" r="16" fill="#1f6dc0" stroke="#dfe6f0" stroke-width="4"/>
          </svg>
          <span class="service-title">BE FOUND</span>
          <span class="service-sub">ON SEEKORA</span>
        </li>
      </ul>
    </section>

    <section class="about">
      <h2>VELTHARION IS AN AUSTRALIAN ONLINE MARKETING SPECIALIST FOR SMALL AND MEDIUM INDUSTRIAL BUSINESSES.</h2>
      <h3>THAT MEANS:</h3>
      <ul class="benefits">
        <li>· WE DO ALL THE WORK RIGHT HERE IN AUSTRALIA</li>
        <li>· WE KEEP THE COSTS DOWN</li>
        <li>· WE UNDERSTAND INDUSTRIAL MARKETS</li>
      </ul>
      <svg class="pin" width="106" height="147" viewBox="0 0 106 147" aria-hidden="true">
        <path d="M53 0C23.7 0 0 23.2 0 52c0 38 53 95 53 95s53-57 53-95C106 23.2 82.3 0 53 0z" fill="var(--brand-red)"/>
        <circle cx="53" cy="54" r="33" fill="#fff"/>
      </svg>
    </section>

    <footer class="contact">
      <div class="rule"></div>
      <div class="contact-details">
        <div>Get in touch to find out more:</div>
        <div><strong>Call 1300 555 014</strong></div>
        <div><strong>Email:</strong> <em>webservices@veltharion-example.com</em></div>
      </div>
      <div class="contact-domain">veltharion-example.com</div>
    </footer>

    <div class="unsubscribe">Don't want to recieve further emails? You can <strong>unsibscribe</strong> <a href="#">here</a></div>
  </main>
</div>
</body>
</html>
```